Business Card Design - R.T. Custom Cabinets Ltd.

Design a business card, including a new logo for a new company in Vancouver, British Columbia, Canada.

The logo must be available as a separate file.

The card should include all company information including:
R.T. Custom Cabinets Ltd.
2786 Larchmoor Crescent
Burnaby, B.C. V7K 2P9
Telehone: 604-XXX-XXXX
Fax: 604-XXX-XXXX
www.rtcustomcabinets.example

As well as individual contact information for employees:
Name
Position
Telephone
Email

The card must include a thoughtful message as well

Target Market(s)

Custom Cabinets

Industry/Entity Type

Business

Contact Information for Business Card

Important information on the front, thoughtful message on the back

Colors
fbed22
9bcb3c
0355a3
ec1f27

Requirements
Must have
• See project description
Nice to have
• images that showcase custom cabinets (european, modern and traditional) styles

```html
<!DOCTYPE html>
<html lang="en">
<head>
<meta charset="utf-8">
<title>R.T. Custom Cabinets Ltd. – Business Card</title>
<link href="https://fonts.googleapis.com/css2?family=Open+Sans:wght@400;600;700&display=swap" rel="stylesheet">
<style>
  :root {
    --brand-blue: #0b56a5;
    --ink-dark: #444444;
    --swoosh-grey: #3f3f3f;
    --logo-grey: #c9c9c9;
    --paper: #ffffff;
    --backdrop: #e6e6e6;
  }
  * { margin: 0; padding: 0; box-sizing: border-box; }
  html, body { width: 1000px; height: 1200px; overflow: hidden; }
  body {
    background: var(--backdrop);
    font-family: "Open Sans", Arial, sans-serif;
    position: relative;
  }
  .card { position: absolute; overflow: hidden; }
  .card-front { left: 75px; top: 32px; width: 850px; height: 553px; background: var(--brand-blue); }
  .card-back { left: 75px; top: 620px; width: 848px; height: 548px; background: var(--paper); }
  .card-shapes { position: absolute; inset: 0; width: 100%; height: 100%; }

  .logo-mark {
    position: absolute; display: flex; flex-direction: column;
    align-items: center; justify-content: center; text-align: center;
    font-weight: 700;
  }
  .card-front .logo-mark { left: 332px; top: 112px; width: 186px; height: 186px; color: var(--paper); }
  .card-back .logo-mark { left: 540px; top: 77px; width: 236px; height: 236px; color: var(--logo-grey); }
  .logo-initials { font-size: 58px; line-height: 1; letter-spacing: 1px; }
  .card-back .logo-initials { font-size: 74px; }
  .logo-tagline { font-size: 12px; margin-top: 8px; letter-spacing: 1px; }
  .card-back .logo-tagline { font-size: 16px; margin-top: 10px; letter-spacing: 1.5px; }

  .company-name {
    position: absolute; left: 0; width: 100%; top: 300px;
    text-align: center; color: var(--paper);
    font-size: 28px; font-weight: 700;
  }

  .contact-list { position: absolute; list-style: none; }
  .contact-item { display: flex; align-items: flex-start; gap: 10px; font-size: 15px; line-height: 18px; }
  .contact-icon { width: 20px; height: 20px; flex: none; margin-top: -1px; }
  .card-front .contact-list { left: 563px; top: 462px; color: var(--paper); }
  .card-front .contact-item + .contact-item { margin-top: 24px; }

  .person-name {
    position: absolute; left: 85px; top: 150px;
    color: var(--brand-blue); font-size: 42px; font-weight: 700; letter-spacing: 0.5px;
  }
  .person-position {
    position: absolute; left: 88px; top: 200px;
    color: var(--ink-dark); font-size: 22px; font-weight: 700;
  }
  .card-back .personal-contacts { left: 85px; top: 258px; color: var(--brand-blue); }
  .card-back .personal-contacts .contact-item + .contact-item { margin-top: 20px; }
  .card-back .company-contacts { left: 566px; top: 411px; color: var(--paper); }
  .card-back .company-contacts .contact-item + .contact-item { margin-top: 15px; }
</style>
</head>
<body>

<section class="card card-front" aria-label="Card front">
  <svg class="card-shapes" viewBox="0 0 850 553" aria-hidden="true">
    <circle cx="425" cy="205" r="93" fill="none" stroke="#ffffff" stroke-width="5"/>
    <path d="M0,476 C225,473 525,388 850,338 C525,398 225,513 0,508 Z" fill="#ffffff"/>
  </svg>
  <div class="logo-mark">
    <span class="logo-initials">R.T.</span>
    <span class="logo-tagline">Custom Cabinets</span>
  </div>
  <p class="company-name">R.T. Custom Cabinets Ltd.</p>
  <ul class="contact-list">
    <li class="contact-item">
      <svg class="contact-icon" viewBox="0 0 20 20" aria-hidden="true"><circle cx="10" cy="10" r="10" fill="#fff"/><path d="M6.5,5 L8.5,5 L9.3,7.6 L8,8.6 C8.7,10.2 9.8,11.3 11.4,12 L12.4,10.7 L15,11.5 L15,13.5 C15,14.2 14.4,14.8 13.7,14.7 C9.5,14.3 5.7,10.5 5.3,6.3 C5.2,5.6 5.8,5 6.5,5 Z" fill="#0b56a5"/></svg>
      <span>604-XXX-XXXX</span>
    </li>
    <li class="contact-item">
      <svg class="contact-icon" viewBox="0 0 20 20" aria-hidden="true"><circle cx="10" cy="10" r="10" fill="#fff"/><circle cx="10" cy="10" r="5.5" fill="none" stroke="#0b56a5" stroke-width="1.4"/><path d="M4.5,10 H15.5 M10,4.5 C7.5,7.5 7.5,12.5 10,15.5 M10,4.5 C12.5,7.5 12.5,12.5 10,15.5" fill="none" stroke="#0b56a5" stroke-width="1.2"/></svg>
      <span>www.rtcustomcabinets.example</span>
    </li>
  </ul>
</section>

<section class="card card-back" aria-label="Card back">
  <svg class="card-shapes" viewBox="0 0 848 548" aria-hidden="true">
    <circle cx="658" cy="195" r="118" fill="none" stroke="#d4d4d4" stroke-width="3"/>
    <path d="M0,505 C275,485 575,380 848,335 L848,548 L0,548 Z" fill="#0b56a5"/>
    <path d="M0,465 C275,460 575,380 848,335 C575,392 275,500 0,505 Z" fill="#3f3f3f"/>
  </svg>
  <div class="logo-mark">
    <span class="logo-initials">R.T.</span>
    <span class="logo-tagline">Custom Cabinets</span>
  </div>
  <h1 class="person-name">NAME IS HERE</h1>
  <p class="person-position">POSITION</p>
  <ul class="contact-list personal-contacts">
    <li class="contact-item">
      <svg class="contact-icon" viewBox="0 0 20 20" aria-hidden="true"><circle cx="10" cy="10" r="10" fill="#0b56a5"/><path d="M6.5,5 L8.5,5 L9.3,7.6 L8,8.6 C8.7,10.2 9.8,11.3 11.4,12 L12.4,10.7 L15,11.5 L15,13.5 C15,14.2 14.4,14.8 13.7,14.7 C9.5,14.3 5.7,10.5 5.3,6.3 C5.2,5.6 5.8,5 6.5,5 Z" fill="#fff"/></svg>
      <span>XXX-XXXX</span>
    </li>
    <li class="contact-item">
      <svg class="contact-icon" viewBox="0 0 20 20" aria-hidden="true"><circle cx="10" cy="10" r="10" fill="#0b56a5"/><rect x="5" y="6.5" width="10" height="7" fill="#fff"/><path d="M5,6.5 L10,10.5 L15,6.5" fill="none" stroke="#0b56a5" stroke-width="1.2"/></svg>
      <span>XXX@rtcustomcabinets.example</span>
    </li>
  </ul>
  <ul class="contact-list company-contacts">
    <li class="contact-item">
      <svg class="contact-icon" viewBox="0 0 20 20" aria-hidden="true"><circle cx="10" cy="10" r="10" fill="#fff"/><path d="M10,4.5 C7.6,4.5 6,6.2 6,8.4 C6,11 10,15.5 10,15.5 C10,15.5 14,11 14,8.4 C14,6.2 12.4,4.5 10,4.5 Z" fill="#0b56a5"/><circle cx="10" cy="8.4" r="1.6" fill="#fff"/></svg>
      <span>2786 Larchmoor Crescent<br>Burnaby, B.C. V7K 2P9</span>
    </li>
    <li class="contact-item">
      <svg class="contact-icon" viewBox="0 0 20 20" aria-hidden="true"><circle cx="10" cy="10" r="10" fill="#fff"/><rect x="7" y="4.5" width="6" height="3" fill="#0b56a5"/><rect x="5" y="8" width="10" height="5" rx="1" fill="#0b56a5"/><rect x="7" y="11.5" width="6" height="4" fill="#0b56a5" stroke="#fff" stroke-width="0.8"/></svg>
      <span>604-XXX-XXXX</span>
    </li>
    <li class="contact-item">
      <svg class="contact-icon" viewBox="0 0 20 20" aria-hidden="true"><circle cx="10" cy="10" r="10" fill="#fff"/><circle cx="10" cy="10" r="5.5" fill="none" stroke="#0b56a5" stroke-width="1.4"/><path d="M4.5,10 H15.5 M10,4.5 C7.5,7.5 7.5,12.5 10,15.5 M10,4.5 C12.5,7.5 12.5,12.5 10,15.5" fill="none" stroke="#0b56a5" stroke-width="1.2"/></svg>
      <span>www.rtcustomcabinets.example</span>
    </li>
  </ul>
</section>

</body>
</html>
```